Kestrelwood Pathways Agency business cards

Australian company about to start offering its services. We recruit international students to come to study English, vocational education and postgraduate courses in Australia. We help them find the institution and select the right city they want to come to Australia. We are a young, online oriented and supportive agency. Our clients are between 18 and 35 years old, mainly University students, young professionals or people with work experience. We provide much more information that any other agency offer. We administrate a Facebook group with more than 11.000 members that daily ask questions about general information when coming to Australia, while they are here and even after they leave the country

Target Market(s)

International students from South America, Central America and Europe

Industry/Entity Type

Student

Contact Information for Business Card

Tomas Brevik
Managing Director
tomas@velmorin.com.au
www.velmorin.com.au
+61 491058263
Melbourne, Australia

Font styles to use
Serif
Sans Serif

Colors

Designer to choose colors to be used in the design.

Requirements
Must have
• Horizontal design
• Standard business card size and shape. If font uses green or yellow colours, they will have to match the ones from the logo
Nice to have
• UPDATE: Use the contents of the green image to design one of the card sides. Use our logo in the background of that side as watermark.
• Passport image, or immigration stamps. A picture of the Yarra River (from Melbourne) would be cool as well.
Should not have
• Non-standard business card size and shape
• Not black as the background colour of any sides as we are not a VIP agency or a hight class service. We are orientes to young people and they like colours, pictures, something attractive.
• Vertical design
• NO YELLOW or BLACK AS THE BACKGROUND COLOUR OF ANY SIDE OF THE BIZ CARD

```html
<!DOCTYPE html>
<html lang="en">
<head>
<meta charset="utf-8">
<title>Kestrelwood Pathways Agency – Business Cards</title>
<link href="https://fonts.googleapis.com/css2?family=Quicksand:wght@400;500;700&display=swap" rel="stylesheet">
<style>
  :root {
    --backdrop: #e4e4e4;
    --card: #ffffff;
    --brand-green: #1d6a3a;
    --brand-yellow: #e3bd1f;
    --text-strong: #7b7b7b;
    --text-soft: #8f8f8f;
    --icon: #9a9a9a;
  }
  * { box-sizing: border-box; margin: 0; padding: 0; }
  html, body {
    width: 1200px;
    height: 800px;
    overflow: hidden;
    background: var(--backdrop);
    font-family: "Quicksand", sans-serif;
  }
  .canvas {
    position: relative;
    width: 1200px;
    height: 800px;
  }
  .card {
    position: absolute;
    width: 540px;
    height: 328px;
    background: var(--card);
    box-shadow: 0 6px 18px rgba(0,0,0,0.12);
    overflow: hidden;
  }
  .card--front { left: 580px; top: 60px; }
  .card--back  { left: 80px;  top: 410px; }

  .card__band {
    position: absolute;
    left: 0; right: 0; bottom: 0;
    height: 16px;
    display: flex;
  }
  .card__band-yellow { background: var(--brand-yellow); width: 52%; }
  .card__band-green  { background: var(--brand-green); flex: 1; }

  .wordmark {
    display: flex;
    align-items: center;
    gap: 10px;
    color: var(--brand-green);
    font-weight: 700;
    letter-spacing: 0.5px;
  }
  .wordmark__dot {
    width: 18px; height: 18px;
    border-radius: 50%;
    background: var(--brand-yellow);
  }
  .card--front .wordmark {
    position: absolute;
    left: 0; right: 0; top: 118px;
    justify-content: center;
    font-size: 52px;
  }
  .card--back .wordmark {
    position: absolute;
    left: 34px; top: 66px;
    font-size: 40px;
  }
  .card--back .wordmark__dot { width: 14px; height: 14px; }

  .contact {
    position: absolute;
    left: 286px;
    top: 134px;
  }
  .contact__name {
    font-size: 25px;
    font-weight: 700;
    color: var(--text-strong);
    line-height: 1.1;
  }
  .contact__role {
    font-size: 19px;
    font-weight: 400;
    color: var(--text-soft);
    margin-bottom: 16px;
  }
  .contact__list { list-style: none; }
  .contact__item {
    display: flex;
    align-items: center;
    gap: 12px;
    font-size: 13.5px;
    color: var(--text-soft);
    line-height: 20px;
  }
  .contact__icon {
    width: 12px; height: 12px;
    flex: none;
    fill: none;
    stroke: var(--icon);
    stroke-width: 1.4;
  }
</style>
</head>
<body>
<main class="canvas">

  <section class="card card--front" aria-label="Business card front">
    <div class="wordmark"><span class="wordmark__dot"></span>Velmorin</div>
    <div class="card__band"><span class="card__band-yellow"></span><span class="card__band-green"></span></div>
  </section>

  <section class="card card--back" aria-label="Business card back">
    <div class="wordmark"><span class="wordmark__dot"></span>Velmorin</div>

    <div class="contact">
      <p class="contact__name">Tomas Brevik</p>
      <p class="contact__role">Managing Director</p>
      <ul class="contact__list">
        <li class="contact__item">
          <svg class="contact__icon" viewBox="0 0 12 12"><rect x="1" y="2.5" width="10" height="7" rx="0.5"/><path d="M1 3l5 3.5L11 3"/></svg>
          tomas@velmorin.com.au
        </li>
        <li class="contact__item">
          <svg class="contact__icon" viewBox="0 0 12 12"><circle cx="6" cy="6" r="5"/><path d="M1 6h10M6 1c-2.5 3-2.5 7 0 10M6 1c2.5 3 2.5 7 0 10"/></svg>
          www.velmorin.com.au
        </li>
        <li class="contact__item">
          <svg class="contact__icon" viewBox="0 0 12 12"><rect x="3" y="0.8" width="6" height="10.4" rx="1"/><path d="M5.2 9.4h1.6"/></svg>
          +61 491058263
        </li>
        <li class="contact__item">
          <svg class="contact__icon" viewBox="0 0 12 12"><path d="M6 11S2 7 2 4.5a4 4 0 0 1 8 0C10 7 6 11 6 11z"/><circle cx="6" cy="4.5" r="1.4"/></svg>
          Melbourne, Australia
        </li>
      </ul>
    </div>

    <div class="card__band"><span class="card__band-yellow"></span><span class="card__band-green"></span></div>
  </section>

</main>
</body>
</html>
```